Radiant Harvest Gathering 2021

I am looking to create a flyer for a one day prayer retreat our church is organizing. This flyer will be posted on social media, websites, mobile apps, and will also be printed so it can be mailed to people.

I am looking for something professional, with good use of our logo and band colors (logo colors).

I am counting on the designer's skill, creativity, art and knowledge of media communication to produce a flyer that will effectively and quickly convey the message we are trying to spread.

CONTENT OF THE FLYER:
Event title: Radiant Harvest Gathering
Date: Tuesday July 2nd, 2021
Time: 11:00AM - 7:00PM
Bellmore Hotel, 4817 Wexley Avenue, Portland, Maine 04109 (Room: Tamarind)
Event Key words to highlight what the event is about: Prayer, Fasting, Worship, Prophecy, Revival.
Key phrases:
A one day prayer retreat.
Jesus Chris is Lord

Contact info:
www.quvello.org
Phone: 207 555 0148
Email: contact@brookmeadow.org

```html
<!DOCTYPE html>
<html lang="en">
<head>
<meta charset="utf-8">
<title>Radiant Harvest Gathering 2021</title>
<link rel="stylesheet" href="https://fonts.googleapis.com/css2?family=Kaushan+Script&family=Orbitron:wght@700;900&family=Cormorant+Garamond:wght@600&family=Open+Sans:wght@700;800&family=Kalam:wght@700&display=swap">
<style>
:root{
  --navy:#1d3855;
  --indigo:#2d3a8c;
  --deep-indigo:#2a237a;
  --addr:#3a4a9a;
  --violet:#3b2f95;
  --orange:#f0962a;
  --ink:#1f3a5a;
  --sky:#9fd3ee;
  --paper:#fbf4d0;
  --white:#ffffff;
}
*{margin:0;padding:0;box-sizing:border-box}
html,body{width:816px;height:1200px;overflow:hidden}
body{position:relative;font-family:"Open Sans",sans-serif;background:#eef3f8}
.backdrop{position:absolute;left:0;top:0;width:816px;height:1028px;
  background:radial-gradient(ellipse at 50% 38%,#dfe4ec 0%,#e9eef5 35%,#f3f6fa 65%,#e6ecf3 100%)}
.tagline{position:absolute;top:58px;width:100%;text-align:center;font-family:"Kaushan Script",cursive;font-size:33px;color:var(--ink)}
.ornament{position:absolute;left:308px;top:110px;width:200px;height:16px;border-radius:8px;background:linear-gradient(90deg,transparent,#b8c3d2,transparent)}
.title{position:absolute;top:176px;width:100%;text-align:center;font-family:"Orbitron",sans-serif;font-weight:900;color:var(--white);
  text-shadow:0 2px 0 #c9c9e6,0 4px 0 var(--violet),0 6px 6px rgba(40,30,120,.45)}
.title .l1{display:block;font-size:44px;letter-spacing:1px;line-height:52px}
.title .l2{display:block;font-size:58px;letter-spacing:2px;line-height:66px}
.subtitle{position:absolute;top:318px;width:100%;text-align:center;font-family:"Cormorant Garamond",serif;font-weight:600;font-size:21px;letter-spacing:9px;color:#2b2f3a}
.date{position:absolute;left:96px;top:548px;color:var(--indigo);font-weight:800;letter-spacing:-3px}
.date .day{display:block;font-size:60px;line-height:70px}
.date .month{display:block;font-size:60px;line-height:70px;padding-left:6px}
.date sup{font-size:28px;letter-spacing:0;vertical-align:28px}
.year{position:absolute;left:384px;top:557px;width:49px;height:128px;background:var(--orange);display:flex;align-items:center;justify-content:center}
.year span{transform:rotate(-90deg);color:var(--white);font-weight:800;font-size:28px;letter-spacing:-1px}
.time{position:absolute;left:440px;top:548px;font-weight:800;font-size:38px;letter-spacing:-2px;color:var(--deep-indigo)}
.venue{position:absolute;left:447px;top:618px;font-weight:700;font-size:15px;line-height:24px;color:var(--addr)}
.notepad{position:absolute;left:290px;top:722px;width:230px;height:268px;background:var(--paper);transform:rotate(-12deg);box-shadow:4px 6px 10px rgba(0,0,0,.15);border-top:10px solid #3d4450;padding:26px 0 0 34px}
.notepad ul{list-style:none;font-family:"Kalam",cursive;font-weight:700;font-size:30px;line-height:42px;color:#1e1e1e}
.notepad li{display:flex;align-items:center;gap:10px}
.notepad svg{width:16px;height:16px;flex:none}
.footer{position:absolute;left:0;top:1028px;width:816px;height:172px;background:var(--navy)}
.brand{position:absolute;left:132px;top:58px;display:flex;align-items:center;gap:10px;color:var(--white);font-weight:700;font-size:30px;letter-spacing:1px}
.brand i{width:18px;height:18px;border-radius:50%;background:var(--orange)}
.call{position:absolute;left:361px;top:37px;width:104px;height:29px;border-radius:6px;background:var(--sky);color:var(--navy);font-weight:800;font-size:19px;text-align:center;line-height:29px}
.phone{position:absolute;left:481px;top:27px;color:var(--white);font-weight:800;font-size:35px;letter-spacing:.5px}
.contacts{position:absolute;left:361px;top:84px;display:flex;align-items:center;gap:6px;color:var(--white);font-weight:700;font-size:15px}
.contacts svg{width:15px;height:15px}
.contacts .gap{width:6px}
</style>
</head>
<body>
<div class="backdrop" role="img" aria-label="Soft icy white background with a faint figure raising both arms in worship"></div>
<p class="tagline">Jesus Christ is Lord</p>
<div class="ornament" role="img" aria-label="Small leafy laurel divider"></div>
<h1 class="title"><span class="l1">RADIANT HARVEST</span><span class="l2">GATHERING</span></h1>
<p class="subtitle">A ONE DAY PRAYER RETREAT</p>
<div class="date"><span class="day">TUESDAY</span><span class="month">JULY 2 <sup>ND</sup></span></div>
<div class="year"><span>2021</span></div>
<p class="time">11:00 AM - 7:00 PM</p>
<p class="venue">BELLMORE HOTEL, 4817 WEXLEY AVENUE<br>PORTLAND, MAINE 04109<br>(ROOM: TAMARIND )</p>
<div class="notepad">
  <ul>
    <li><svg viewBox="0 0 16 16"><path d="M2 8l4 4 8-9" fill="none" stroke="#f0b020" stroke-width="3"/></svg>Prayer</li>
    <li><svg viewBox="0 0 16 16"><path d="M2 8l4 4 8-9" fill="none" stroke="#f0b020" stroke-width="3"/></svg>Fasting</li>
    <li><svg viewBox="0 0 16 16"><path d="M2 8l4 4 8-9" fill="none" stroke="#f0b020" stroke-width="3"/></svg>Worship</li>
    <li><svg viewBox="0 0 16 16"><path d="M2 8l4 4 8-9" fill="none" stroke="#f0b020" stroke-width="3"/></svg>Prophecy</li>
    <li><svg viewBox="0 0 16 16"><path d="M2 8l4 4 8-9" fill="none" stroke="#f0b020" stroke-width="3"/></svg>Revival</li>
  </ul>
</div>
<footer class="footer">
  <div class="brand"><i></i>QUVELLO</div>
  <div class="call">CALL US</div>
  <div class="phone">207 555 0148</div>
  <div class="contacts">
    <svg viewBox="0 0 16 16"><rect x="1" y="3" width="14" height="10" fill="none" stroke="#f0962a" stroke-width="1.5"/><path d="M1 3l7 6 7-6" fill="none" stroke="#f0962a" stroke-width="1.5"/></svg>
    <span>contact@brookmeadow.org</span><span class="gap"></span>
    <svg viewBox="0 0 16 16"><circle cx="8" cy="8" r="6.5" fill="none" stroke="#f0962a" stroke-width="1.3"/><ellipse cx="8" cy="8" rx="3" ry="6.5" fill="none" stroke="#f0962a" stroke-width="1.3"/><path d="M1.5 8h13" stroke="#f0962a" stroke-width="1.3"/></svg>
    <span>www.quvello.org</span>
  </div>
</footer>
</body>
</html>
```